All About How Do Title Loans Work?*

Hi There,<br/>We: Bright Oak Auto Pawn Lending (Loan agency in the US) are looking to get infographic design services for our most comprehensive guide: How do Title Loans Work. <br/>This guide has 6 steps that describe the title loan process/ service that we offer to our clients. <br/>If you’d like to know how car title loans work, then read this: https://brightoaklend.com/how-do-title-loans-work/

Target Market(s)

Personal Loans in US

Industry/Entity Type

Financial

Requirements
Must have
• Logo
• 1-6 steps
• Apply now + How Much Cash Can I Get https://snapvu.io/q8hxw1 / https://snapvu.io/q8hyz3 (call to action): Find that buttons here: https://brightoaklend.com/can-i-get-a-title-loan-if-the-title-is-not-in-my-name/
• The disclaimers: Please use the disclaimer that appears below the content: examples: https://snapvu.io/q8jk47 https://snapvu.io/q8jm52 https://snapvu.io/q8jn68 etc.
Nice to have
• Dana: https://brightoaklend.com/apply-now/ (our presenter)-> https://snapvu.io/q8hv90
Should not have
• Colors that not related to our website
• Don't promise anything we can't deliver (we have strict guidelines in the loan industry)

```html
<!DOCTYPE html>
<html lang="en">
<head>
<meta charset="utf-8">
<title>How Do Title Loans Work? – Bright Oak Auto Pawn Lending</title>
<link href="https://fonts.googleapis.com/css2?family=Oswald:wght@500;600;700&family=Roboto+Condensed:wght@400;500&family=Roboto:wght@400&display=swap" rel="stylesheet">
<style>
:root{
  --blue:#3a61b3;
  --blue-deep:#2d56a6;
  --yellow:#ffd500;
  --ink:#222a3a;
  --heading:#4d4d52;
  --paper:#f4f4f6;
  --white:#ffffff;
}
*{margin:0;padding:0;box-sizing:border-box}
html,body{width:1200px;height:3509px;overflow:hidden}
body{background:linear-gradient(#f7f7f9,#eeeef2);font-family:"Roboto Condensed",sans-serif;color:var(--ink);position:relative}
.abs{position:absolute}
.vc{transform:translateY(-50%)}
.header-band{left:0;top:0;width:1200px;height:470px;background:var(--blue)}
.brand{left:52px;top:64px;color:var(--white);font-family:"Oswald",sans-serif;font-weight:600;font-size:38px;line-height:1.1;width:440px;letter-spacing:.5px}
.title-top,.title-bottom{left:50px;color:var(--white);font-family:"Oswald",sans-serif;font-weight:600;font-size:52px;letter-spacing:.3px;white-space:nowrap}
.title-top{top:245px}
.title-bottom{top:391px}
.title-main{left:48px;top:318px;color:var(--yellow);font-family:"Oswald",sans-serif;font-weight:700;font-size:92px;white-space:nowrap}
.art{border-radius:24px}
.art-hero{left:540px;top:0;width:640px;height:640px;background:radial-gradient(ellipse at 55% 65%,#2b2f66 0%,#3b4290 35%,rgba(58,97,179,0) 70%);border-radius:0}
.art-cash{left:368px;top:1015px;width:259px;height:197px;background:radial-gradient(ellipse,#f0d99a 0%,#e9a94a 50%,rgba(240,240,240,0) 75%)}
.art-laptop{left:705px;top:983px;width:214px;height:229px;background:linear-gradient(#e9e9ec,#6a6d74 70%,#f2a555)}
.art-car{left:95px;top:1525px;width:314px;height:178px;background:radial-gradient(ellipse,#d8d9dc 0%,#9fa2a7 55%,rgba(240,240,240,0) 80%)}
.art-moneybag{left:191px;top:2288px;width:347px;height:334px;background:radial-gradient(ellipse at 55% 45%,#7a5a30 0%,#a38847 40%,#f4cf3a 62%,rgba(240,240,240,0) 80%)}
.step-title{font-family:"Oswald",sans-serif;font-weight:600;font-size:52px;color:var(--heading);white-space:nowrap;letter-spacing:-.5px}
.step-title sup{font-size:24px;vertical-align:top;position:relative;top:4px;margin-left:3px}
.item{display:flex;align-items:center;gap:16px;font-size:29px;color:var(--ink);white-space:nowrap}
.item .icon{width:68px;height:68px;flex:none}
.item.wrap{white-space:normal;align-items:flex-start;width:640px;line-height:1.35}
.item.wrap .icon{margin-top:-8px}
.money-pill{left:0;top:1818px;width:480px;height:56px;background:var(--yellow);border-radius:0 28px 28px 0;font-family:"Oswald",sans-serif;font-weight:600;font-size:30px;color:var(--ink);line-height:56px;padding-left:62px;white-space:nowrap}
.cta{left:143px;top:3214px;width:917px;height:70px;background:var(--yellow);border-radius:35px;font-family:"Oswald",sans-serif;font-weight:700;font-size:44px;color:#131a3a;text-align:center;line-height:70px;box-shadow:0 10px 14px -8px rgba(0,0,0,.25)}
.footer-band{left:0;top:3323px;width:1200px;height:186px;background:var(--blue)}
.notes{left:50px;top:3352px;color:var(--white);font-family:"Roboto",sans-serif;font-size:20px;line-height:34px;list-style:none}
.notes sup{font-size:13px;margin-right:8px}
svg.flow{position:absolute;left:0;top:0}
</style>
</head>
<body>

<div class="abs header-band"></div>
<div class="abs brand">Bright Oak Auto Pawn Lending</div>
<h1>
  <span class="abs vc title-top">HOW DO TITLE LOANS WORK?</span>
  <span class="abs vc title-main">6 SIMPLE STEPS</span>
  <span class="abs vc title-bottom">TO GETTING CAR TITLE LOANS</span>
</h1>
<div class="abs art art-hero" role="img" aria-label="Illustration of a dark blue convertible sports car with gold coins pouring into a pot"></div>

<div class="abs art art-cash" role="img" aria-label="Illustration of banknotes and stacks of gold coins"></div>
<div class="abs art art-laptop" role="img" aria-label="Illustration of hands typing an application on a laptop"></div>
<div class="abs art art-car" role="img" aria-label="Illustration of a silver sedan seen from the front"></div>
<div class="abs art art-moneybag" role="img" aria-label="Illustration of a money bag with stacks of gold coins"></div>

<svg class="flow" width="1200" height="3509" viewBox="0 0 1200 3509" aria-hidden="true">
  <defs>
    <g id="ring"><circle r="22" fill="#fff" stroke="#2d56a6" stroke-width="6"/><circle r="11" fill="#2d56a6"/></g>
    <g id="chev-down" fill="none" stroke="#2d56a6" stroke-width="3.5"><path d="M-9 -10 L0 -2 L9 -10"/><path d="M-9 -2 L0 6 L9 -2"/><path d="M-9 6 L0 14 L9 6"/></g>
    <g id="chev-right" fill="none" stroke="#2d56a6" stroke-width="3.5"><path d="M-10 -9 L-2 0 L-10 9"/><path d="M-2 -9 L6 0 L-2 9"/><path d="M6 -9 L14 0 L6 9"/></g>
  </defs>
  <g fill="none" stroke="#2d56a6" stroke-width="5">
    <path d="M531 685 H606 Q631 685 631 710 V1190 Q631 1223 664 1223 H930"/>
    <path d="M835 1355 H382 Q357 1355 357 1380 V1470 Q357 1497 330 1497 H95 Q68 1497 68 1524 V1703 Q68 1730 95 1730 H595"/>
    <path d="M1052 1723 H1099 Q1124 1723 1124 1748 V1936 Q1124 1961 1099 1961 H859 Q834 1961 834 1986 V2200 Q834 2236 798 2236 H760"/>
    <path d="M348 2238 H95 Q68 2238 68 2265 V2731 Q68 2758 95 2758 H160"/>
    <path d="M701 2762 H1017 Q1042 2762 1042 2787 V2895"/>
  </g>
  <g fill="#2d56a6">
    <path d="M955 1223 L920 1208 L928 1223 L920 1238Z"/>
    <path d="M620 1730 L585 1715 L593 1730 L585 1745Z"/>
    <path d="M740 2236 L775 2221 L767 2236 L775 2251Z"/>
    <path d="M180 2758 L145 2743 L153 2758 L145 2773Z"/>
    <path d="M1042 2922 L1027 2887 L1042 2895 L1057 2887Z"/>
    <circle cx="700" cy="1355" r="7"/><circle cx="208" cy="1497" r="7"/>
    <circle cx="200" cy="1730" r="7"/><circle cx="455" cy="1730" r="7"/>
    <circle cx="834" cy="2011" r="7"/><circle cx="834" cy="2195" r="7"/>
  </g>
  <use href="#chev-down" x="631" y="855"/>
  <use href="#chev-down" x="68" y="1590"/>
  <use href="#chev-down" x="1124" y="1842"/>
  <use href="#chev-down" x="68" y="2410"/>
  <use href="#chev-right" x="512" y="1355" transform="rotate(180 512 1355)"/>
  <use href="#chev-right" x="326" y="1730"/>
  <use href="#ring" x="511" y="685"/>
  <use href="#ring" x="855" y="1355"/>
  <use href="#ring" x="1032" y="1723"/>
  <use href="#ring" x="368" y="2238"/>
  <use href="#ring" x="681" y="2762"/>

  <g font-family="Oswald, sans-serif" font-weight="700" font-size="268">
    <text x="48" y="708" fill="#ffd500">1</text><text x="58" y="708" fill="#2d56a6">1</text>
    <text x="966" y="1314" fill="#ffd500">2</text><text x="976" y="1314" fill="#2d56a6">2</text>
    <text x="600" y="1832" fill="#ffd500">3</text><text x="610" y="1832" fill="#2d56a6">3</text>
    <text x="440" y="2193" fill="#ffd500">4</text><text x="450" y="2193" fill="#2d56a6">4</text>
    <text x="190" y="2853" fill="#ffd500">5</text><text x="200" y="2853" fill="#2d56a6">5</text>
    <text x="960" y="3173" fill="#ffd500">6</text><text x="970" y="3173" fill="#2d56a6">6</text>
  </g>
</svg>

<h2 class="abs vc step-title" style="left:174px;top:685px">REQUIREMENTS<sup>1</sup></h2>
<h2 class="abs vc step-title" style="left:900px;top:1351px">APPLICATION</h2>
<h2 class="abs vc step-title" style="left:785px;top:1723px">APPROVAL<sup>2</sup></h2>
<h2 class="abs vc step-title" style="left:422px;top:2238px">LOAN FUNDING<sup>4</sup></h2>
<h2 class="abs vc step-title" style="left:391px;top:2762px">REPAYMENTS</h2>
<h2 class="abs vc step-title" style="left:657px;top:3078px">LOAN CLOSURE</h2>

<svg width="0" height="0" style="position:absolute">
  <symbol id="i-base" viewBox="0 0 68 68"><circle cx="34" cy="34" r="33" fill="#3a61b3"/></symbol>
</svg>

<!-- Step 1 requirements -->
<div class="abs vc item" style="left:65px;top:804px"><svg class="icon" viewBox="0 0 68 68"><circle cx="34" cy="34" r="33" fill="#3a61b3"/><rect x="22" y="20" width="22" height="28" rx="2" fill="none" stroke="#fff" stroke-width="2.5"/><circle cx="42" cy="42" r="5" fill="none" stroke="#fff" stroke-width="2.5"/></svg>Personal details</div>
<div class="abs vc item" style="left:65px;top:896px"><svg class="icon" viewBox="0 0 68 68"><circle cx="34" cy="34" r="33" fill="#3a61b3"/><rect x="22" y="18" width="24" height="32" rx="2" fill="none" stroke="#fff" stroke-width="2.5"/><path d="M27 36 h14 M27 42 h10" stroke="#fff" stroke-width="2.5"/></svg>Car details</div>
<div class="abs vc item" style="left:65px;top:986px"><svg class="icon" viewBox="0 0 68 68"><circle cx="34" cy="34" r="33" fill="#3a61b3"/><rect x="20" y="20" width="22" height="26" rx="2" fill="none" stroke="#fff" stroke-width="2.5"/><rect x="34" y="38" width="16" height="9" rx="3" fill="#fff"/></svg>Car title</div>
<div class="abs vc item" style="left:65px;top:1079px"><svg class="icon" viewBox="0 0 68 68"><circle cx="34" cy="34" r="33" fill="#3a61b3"/><rect x="19" y="23" width="30" height="22" rx="3" fill="none" stroke="#fff" stroke-width="2.5"/><circle cx="28" cy="32" r="4" fill="#fff"/><path d="M36 30h9M36 37h9" stroke="#fff" stroke-width="2.5"/></svg>Identification</div>
<div class="abs vc item" style="left:65px;top:1170px"><svg class="icon" viewBox="0 0 68 68"><circle cx="34" cy="34" r="33" fill="#3a61b3"/><text x="17" y="45" font-family="Oswald,sans-serif" font-size="30" fill="#fff">$</text><circle cx="42" cy="38" r="8" fill="none" stroke="#fff" stroke-width="2.5"/></svg>Regular income</div>
<div class="abs vc item" style="left:65px;top:1263px"><svg class="icon" viewBox="0 0 68 68"><circle cx="34" cy="34" r="33" fill="#3a61b3"/><circle cx="26" cy="28" r="5" fill="none" stroke="#fff" stroke-width="2.5"/><path d="M17 46 q9 -12 18 0" fill="none" stroke="#fff" stroke-width="2.5"/><rect x="36" y="20" width="15" height="11" rx="2" fill="none" stroke="#fff" stroke-width="2.5"/></svg>References</div>

<div class="abs vc item" style="left:719px;top:707px"><svg class="icon" viewBox="0 0 68 68"><circle cx="34" cy="34" r="33" fill="#3a61b3"/><path d="M24 20 l6 -1 4 9 -4 3 q3 7 10 10 l3 -4 9 4 -1 6 q-2 3 -6 3 q-22 -4 -24 -24 q0 -4 3 -6z" fill="none" stroke="#fff" stroke-width="2.5"/></svg>Call us: (877) 402 6618</div>
<div class="abs vc item" style="left:719px;top:804px"><svg class="icon" viewBox="0 0 68 68"><circle cx="34" cy="34" r="33" fill="#3a61b3"/><path d="M34 50 q-12 -13 -12 -21 a12 12 0 0 1 24 0 q0 8 -12 21z" fill="none" stroke="#fff" stroke-width="2.5"/><circle cx="34" cy="29" r="4" fill="#fff"/></svg>Visit one of our branches</div>
<div class="abs vc item" style="left:719px;top:900px"><svg class="icon" viewBox="0 0 68 68"><circle cx="34" cy="34" r="33" fill="#3a61b3"/><rect x="19" y="22" width="30" height="20" rx="2" fill="none" stroke="#fff" stroke-width="2.5"/><path d="M28 48h12M34 42v6" stroke="#fff" stroke-width="2.5"/></svg>Apply online in 4 easy steps</div>

<!-- Step 2 application -->
<div class="abs item wrap" style="left:418px;top:1422px"><svg class="icon" viewBox="0 0 68 68"><circle cx="34" cy="34" r="33" fill="#3a61b3"/><circle cx="36" cy="27" r="8" fill="none" stroke="#fff" stroke-width="2.5"/><path d="M17 44 h10 l8 4 h12" fill="none" stroke="#fff" stroke-width="2.5"/></svg><span>Title Loans Ranging from 25% to 120% of the Car’s Value</span></div>
<div class="abs item wrap" style="left:418px;top:1525px"><svg class="icon" viewBox="0 0 68 68"><circle cx="34" cy="34" r="33" fill="#3a61b3"/><rect x="24" y="18" width="22" height="22" rx="2" fill="none" stroke="#fff" stroke-width="2.5"/><path d="M17 46 h12 l6 -6" fill="none" stroke="#fff" stroke-width="2.5"/></svg><span>A GPS tracking instrument will be installed in your vehicle <sup>3</sup></span></div>

<!-- Step 3/4 money options -->
<div class="abs money-pill">Get Your Title Loan’s Money</div>
<div class="abs vc item" style="left:68px;top:1934px"><svg class="icon" viewBox="0 0 68 68"><circle cx="34" cy="34" r="33" fill="#3a61b3"/><path d="M19 28 h30 l-3 -8 h-24z M22 28 v18 h24 v-18" fill="none" stroke="#fff" stroke-width="2.5"/></svg>Branch stores</div>
<div class="abs vc item" style="left:68px;top:2036px"><svg class="icon" viewBox="0 0 68 68"><circle cx="34" cy="34" r="33" fill="#3a61b3"/><circle cx="34" cy="34" r="13" fill="none" stroke="#fff" stroke-width="3"/><circle cx="34" cy="34" r="4" fill="#fff"/></svg>CashRelay</div>
<div class="abs vc item" style="left:68px;top:2138px"><svg class="icon" viewBox="0 0 68 68"><circle cx="34" cy="34" r="33" fill="#3a61b3"/><path d="M18 28 l16 -9 16 9z M22 31v12M30 31v12M38 31v12M46 31v12M18 47h32" fill="none" stroke="#fff" stroke-width="2.5"/></svg>Direct deposit</div>

<!-- Step 5 repayments -->
<div class="abs vc item" style="left:719px;top:2340px"><svg class="icon" viewBox="0 0 68 68"><circle cx="34" cy="34" r="33" fill="#3a61b3"/><rect x="26" y="17" width="16" height="34" rx="3" fill="none" stroke="#fff" stroke-width="2.5"/><circle cx="34" cy="46" r="1.8" fill="#fff"/></svg>By Phone</div>
<div class="abs vc item" style="left:719px;top:2449px"><svg class="icon" viewBox="0 0 68 68"><circle cx="34" cy="34" r="33" fill="#3a61b3"/><rect x="24" y="20" width="26" height="18" rx="2" fill="none" stroke="#fff" stroke-width="2.5"/><path d="M16 46 h10 l10 -6" fill="none" stroke="#fff" stroke-width="2.5"/></svg>Online payments</div>
<div class="abs vc item" style="left:719px;top:2558px"><svg class="icon" viewBox="0 0 68 68"><circle cx="34" cy="34" r="33" fill="#3a61b3"/><rect x="17" y="24" width="34" height="20" rx="2" fill="none" stroke="#fff" stroke-width="2.5"/><circle cx="34" cy="34" r="5" fill="#fff"/></svg>Cash payments</div>
<div class="abs vc item" style="left:719px;top:2663px"><svg class="icon" viewBox="0 0 68 68"><circle cx="34" cy="34" r="33" fill="#3a61b3"/><path d="M18 30 v16 h32 v-16 l-16 -10z M18 30 l16 10 16 -10" fill="none" stroke="#fff" stroke-width="2.5"/></svg>Check or money order</div>

<!-- Step 6 closure -->
<div class="abs vc item" style="left:95px;top:2946px"><svg class="icon" viewBox="0 0 68 68"><circle cx="34" cy="34" r="33" fill="#3a61b3"/><path d="M34 40 q-9 -9 -9 -15 a9 9 0 0 1 18 0 q0 6 -9 15z M18 48 h32" fill="none" stroke="#fff" stroke-width="2.5"/></svg>Remove GPS tracking device</div>
<div class="abs vc item" style="left:593px;top:2946px"><svg class="icon" viewBox="0 0 68 68"><circle cx="34" cy="34" r="33" fill="#3a61b3"/><rect x="24" y="26" width="22" height="20" rx="2" fill="none" stroke="#fff" stroke-width="2.5"/><path d="M18 30 a16 16 0 0 1 26 -10" fill="none" stroke="#fff" stroke-width="2.5"/></svg>Get your title returned</div>

<div class="abs cta">APPLY ONLINE or CALL US: (877) 402 6618</div>

<div class="abs footer-band"></div>
<ol class="abs notes">
  <li><sup>1</sup>There is a chance you’ll need to show additional documents.</li>
  <li><sup>2</sup>All loan applications are subject to meeting our credit criteria, which includes applicant’s ability to repay the loan.</li>
  <li><sup>3</sup>You are using your car as collateral against a title loan.</li>
  <li><sup>4</sup>Certain debit and pre-paid cards are not eligible for this type of transaction.</li>
</ol>

</body>
</html>
```